Verdant Press Bottle Label

I am looking to design a bottle for my company verdant press. I have attached the Logo. I would like a label that would include the following.
Name of Juice - K7
Company Logo - attached
Ingredients - Kale,Broccoli, Spinach, Apple, and Cucumber
Health Benefits - K7 is a combination of fruits and vegetables specifically designed to ouwefo wjnwj ekw ckjbewj jw cejnvej (The exact verbage will be added later its the design and look that matters right now)
The bottle it needs to fit on is 6 inches tall and 2 1/4 square (It's the middle bottle in the picture attached.
I am looking for a label that matches the logo.
Thanks.

```html
<!DOCTYPE html>
<html lang="en">
<head>
<meta charset="utf-8">
<title>Verdant Press — K7 Bottle Label</title>
<link rel="stylesheet" href="https://fonts.googleapis.com/css2?family=Bebas+Neue&display=swap">
<style>
  :root {
    --backdrop: #f4f4f2;
    --kraft: #aba396;
    --ink: #111111;
    --rule: #141414;
  }
  html, body {
    margin: 0;
    padding: 0;
    width: 1200px;
    height: 1000px;
    overflow: hidden;
    background: var(--backdrop);
  }
  .canvas {
    position: relative;
    width: 1200px;
    height: 1000px;
  }
  .label {
    position: absolute;
    left: 283px;
    top: 108px;
    width: 634px;
    height: 785px;
    background: var(--kraft);
    font-family: "Bebas Neue", "Oswald", sans-serif;
    color: var(--ink);
  }
  .rule-vertical {
    position: absolute;
    left: 290px;
    top: 0;
    width: 10px;
    height: 100%;
    background: var(--rule);
  }
  .rule-horizontal {
    position: absolute;
    left: 0;
    top: 316px;
    width: 300px;
    height: 10px;
    background: var(--rule);
  }
  .juice-name {
    position: absolute;
    right: 352px;
    top: 118px;
    margin: 0;
    font-size: 150px;
    line-height: 1;
    font-weight: 400;
  }
  .ingredients {
    position: absolute;
    right: 362px;
    top: 360px;
    margin: 0;
    padding: 0;
    list-style: none;
    text-align: right;
    font-size: 58px;
    line-height: 58px;
  }
  .benefits {
    position: absolute;
    left: 340px;
    top: 352px;
    height: 290px;
    margin: 0;
    writing-mode: vertical-rl;
    font-size: 23px;
    line-height: 31px;
    letter-spacing: 0.3px;
    text-transform: uppercase;
  }
  .brand {
    position: absolute;
    left: 362px;
    top: 680px;
    display: flex;
    align-items: center;
    gap: 10px;
    font-size: 36px;
    line-height: 1;
  }
  .brand-dot {
    width: 22px;
    height: 22px;
    border-radius: 50%;
    background: var(--ink);
  }
</style>
</head>
<body>
  <main class="canvas">
    <section class="label" aria-label="K7 juice bottle label">
      <div class="rule-vertical"></div>
      <div class="rule-horizontal"></div>
      <h1 class="juice-name">K7</h1>
      <ul class="ingredients">
        <li>Kale</li>
        <li>Broccoli</li>
        <li>Spinach</li>
        <li>Apple</li>
        <li>Cucumber</li>
      </ul>
      <p class="benefits">K7 is a combination of fruits and vegetables specifically designed to ouwefo wjnwj ekw ckjbewj jw cejnvej (the exact verbage will be added later its the design and look that matters right now)</p>
      <div class="brand">
        <span class="brand-dot"></span>
        <span class="brand-name">Verdant Press</span>
      </div>
    </section>
  </main>
</body>
</html>
```